Taveno Professional Services Website

Small website for company presence and information. Company is an IT/Telecom services company. We provide presales and installation services. Included are various company logos including color levels. Site doesn't have to use these exact colors in the logos, but should be complimentary if using different colors. It should have a professional business appearance.
Updates

My apologies for not being more responsive on the designs that have been submitted. I will be narrowing down the submissions and providing additional feedback next week. Thank you for your patience.

Project Deadline Extended
Reason: Sorry again for delays on picking designs. Work has me very busy and I've just not had the time to devote to this project. I am extending the design deadline for a few more days to give me time to make my final decisions. Thank you all for your patience. Stay tuned....

Target Market(s)

Telecom sales companies that sell Brintel telecom products.

Industry/Entity Type

Professional Service

Coding

Coded - Design and coding required

Number of Pages Required

5+ page

Font styles to use
Sans Serif

Colors
3276b5
0355a3
85abd2
85cae6
33a6d7
0692cd
ffffff

Requirements
Must have
• Professional design reflective of IT/Telecom business. A good reference website would be: http://www.quollanetworks.example/. Looking for something similar in function and presence.
Nice to have
• Rolling photos highlighting our services. Traditional navigation across the top of all pages.
Should not have
• No motion video, flashy presentation or overly confused interface.

```html
<!DOCTYPE html>
<html lang="en">
<head>
<meta charset="utf-8">
<title>Taveno Professional Services</title>
<link href="https://fonts.googleapis.com/css2?family=Open+Sans:wght@400;600;700&display=swap" rel="stylesheet">
<style>
:root{
  --ink:#1f2226;
  --body:#3a3d42;
  --muted:#55595f;
  --nav:#2f3033;
  --nav-line:#1c1d1f;
  --accent:#3276b5;
  --accent-bright:#4f8de8;
  --hero-dark:#123a63;
  --hero-mid:#2d5f8e;
  --hero-light:#7fa3c4;
  --page:#e9ecef;
  --page-alt:#dcdfe2;
  --page-soft:#e4e7ea;
  --card:#e2e6ec;
  --field:#f4f5f6;
  --field-line:#c9ccd0;
  --footer:#121314;
  --white:#ffffff;
}
*{box-sizing:border-box;margin:0;padding:0}
html,body{width:1200px;height:3253px;overflow:hidden}
body{font-family:"Open Sans",Arial,sans-serif;color:var(--ink);background:var(--page);position:relative}
h1,h2,h3,h4{font-weight:400}
.block{position:absolute;left:0;width:1200px}

/* hero */
.hero{top:0;height:443px;background:radial-gradient(ellipse at 45% 40%,var(--hero-light) 0%,var(--hero-mid) 40%,var(--hero-dark) 100%)}
.hero-title{position:absolute;top:168px;width:100%;text-align:center;color:var(--white);font-size:68px;font-weight:600;line-height:84px}
.hero-sub{position:absolute;top:272px;width:100%;text-align:center;color:var(--white);font-size:32px;font-weight:600;line-height:44px}

/* navigation */
.nav{top:443px;height:43px;background:var(--nav);border-top:2px solid var(--nav-line)}
.brand{position:absolute;left:110px;top:7px;display:flex;align-items:center;gap:9px;color:var(--white);font-size:21px;font-weight:700;letter-spacing:1px;line-height:26px}
.brand-dot{width:26px;height:26px;border-radius:50%;background:var(--accent)}
.menu{position:absolute;left:380px;top:0;display:flex;gap:25px;list-style:none}
.menu li{color:var(--white);font-size:12.5px;line-height:41px}

/* sections */
.profile{top:486px;height:558px;background:var(--page)}
.team{top:1044px;height:822px;background:var(--page-alt)}
.team-note{position:absolute;top:586px;left:0;width:1200px;height:236px;background:var(--page-soft)}
.services{top:1866px;height:712px;background:var(--page)}
.queries{top:2578px;height:271px;background:var(--page-alt)}
.contact{top:2849px;height:350px;background:var(--page-soft)}

.heading{position:absolute;width:100%;text-align:center;font-size:52px;font-weight:400;line-height:64px;color:var(--ink)}
.lead{position:absolute;left:260px;width:680px;text-align:center;font-size:15px;font-weight:600;line-height:35px;color:var(--ink)}
.subheading{position:absolute;width:100%;text-align:center;font-size:26px;font-weight:400;line-height:34px;color:var(--ink)}
.copy{position:absolute;left:100px;width:1000px;text-align:center;font-size:11.5px;line-height:25.5px;color:var(--muted)}

/* team */
.member{position:absolute;top:295px;width:224px;height:223px;background:linear-gradient(180deg,#8fb3b8 0%,#c9d3d6 45%,#5e6b73 100%)}
.member-label{position:absolute;left:0;top:128px;width:100%;height:63px;background:var(--accent-bright);opacity:.92;color:var(--white);text-align:center;padding-top:5px}
.member-name{font-size:17px;font-weight:600;line-height:27px}
.member-role{font-size:17px;line-height:27px}

/* services */
.service{position:absolute;top:297px;width:224px;height:324px;background:var(--card);border-radius:9px;text-align:center}
.service svg{position:absolute;left:84px;top:20px}
.service-title{position:absolute;top:98px;width:100%;font-size:20px;font-weight:400;line-height:26px;color:var(--ink)}
.service-text{position:absolute;left:22px;width:180px;font-size:12px;line-height:26px;color:var(--muted)}

/* contact */
.contact-title{position:absolute;left:98px;top:56px;font-size:20px;font-weight:400;color:var(--ink)}
.contact-list{position:absolute;left:98px;top:100px;list-style:none}
.contact-list li{display:flex;align-items:center;gap:7px;font-size:16px;line-height:35px;color:var(--body)}
.social{position:absolute;left:98px;top:244px;display:flex;gap:14px}
.social span{width:24px;height:24px;border-radius:50%;background:var(--body)}
.form-title{position:absolute;left:527px;top:52px;font-size:27px;font-weight:400;color:var(--ink)}
.form-copy{position:absolute;left:527px;top:94px;width:575px;font-size:11.5px;line-height:23px;color:var(--muted)}
.field{position:absolute;background:var(--field);border:1px solid var(--field-line);font-size:11px;color:#8a8e93;padding:4px 9px}
.button{position:absolute;left:527px;top:309px;width:112px;height:27px;background:var(--field);border:1px solid var(--field-line);border-radius:2px;font-size:12px;line-height:25px;text-align:center;color:var(--body)}

.footer{top:3199px;height:54px;background:var(--footer)}
.footer-note{position:absolute;right:45px;top:18px;font-size:12px;color:var(--white)}
</style>
</head>
<body>

<header class="block hero" role="img" aria-label="Blue world map with glowing network connection lines">
  <h1 class="hero-title">We provide</h1>
  <p class="hero-sub">presales and installation services</p>
</header>

<nav class="block nav">
  <div class="brand"><span class="brand-dot"></span>TAVENO</div>
  <ul class="menu"><li>HOME</li><li>ABOUT</li><li>TEAM</li><li>SERVICES</li><li>CONTACT</li></ul>
</nav>

<section class="block profile">
  <h2 class="heading" style="top:58px">Company's Profile</h2>
  <p class="lead" style="top:142px">Lorem ipsum dolor sit amet, consectetur adipiscing elit. Curabitur nec nisl odio. Mauris vehicula at nunc id posuere.</p>
  <h3 class="subheading" style="top:270px">Lorem ipsum dolor sit amet</h3>
  <p class="copy" style="top:310px">Lorem ipsum dolor sit amet, consectetur adipiscing elit. Curabitur nec nisl odio. Mauris vehicula at nunc id posuere. Lorem ipsum dolor sit amet, consectetur adipiscing elit. Curabitur nec nisl odio. Mauris vehicula at nunc id posuere. Lorem ipsum dolor sit amet, consectetur adipiscing elit. Curabitur nec nisl odio. Mauris vehicula at nunc id posuere. Lorem ipsum dolor sit amet, consectetur adipiscing elit. Curabitur nec nisl odio. Mauris vehicula at nunc id posuere. Lorem ipsum dolor sit amet, consectetur adipiscing elit. Curabitur nec nisl odio. Mauris vehicula at nunc id posuere. Lorem ipsum dolor sit amet, consectetur adipiscing elit. Curabitur nec nisl odio. Mauris vehicula at nunc id posuere. Lorem ipsum dolor sit amet, consectetur adipiscing elit. Curabitur nec nisl odio. Mauris vehicula at nunc id posuere. Lorem ipsum dolor sit amet, consectetur adipiscing elit. Curabitur nec nisl odio. Mauris vehicula at nunc id posuere. Lorem ipsum dolor sit amet, consectetur adipiscing elit. Curabitur nec nisl odio. Mauris vehicula at nunc id posuere.</p>
</section>

<section class="block team">
  <div class="team-note"></div>
  <h2 class="heading" style="top:98px">Who We Are ?</h2>
  <p class="lead" style="top:182px">Lorem ipsum dolor sit amet, consectetur adipiscing elit. Curabitur nec nisl odio. Mauris vehicula at nunc id posuere.</p>

  <div class="member" style="left:113px" role="img" aria-label="Portrait photo of a team member in an office">
    <div class="member-label"><div class="member-name">NAME SURNAME</div><div class="member-role">POSITION</div></div>
  </div>
  <div class="member" style="left:363px" role="img" aria-label="Portrait photo of a team member in an office">
    <div class="member-label"><div class="member-name">NAME SURNAME</div><div class="member-role">POSITION</div></div>
  </div>
  <div class="member" style="left:614px" role="img" aria-label="Portrait photo of a team member in an office">
    <div class="member-label"><div class="member-name">NAME SURNAME</div><div class="member-role">POSITION</div></div>
  </div>
  <div class="member" style="left:864px" role="img" aria-label="Portrait photo of a team member in an office">
    <div class="member-label"><div class="member-name">NAME SURNAME</div><div class="member-role">POSITION</div></div>
  </div>

  <h3 class="subheading" style="top:598px">Lorem ipsum dolor sit amet</h3>
  <p class="copy" style="top:636px">Lorem ipsum dolor sit amet, consectetur adipiscing elit. Curabitur nec nisl odio. Mauris vehicula at nunc id posuere. Lorem ipsum dolor sit amet, consectetur adipiscing elit. Curabitur nec nisl odio. Mauris vehicula at nunc id posuere. Lorem ipsum dolor sit amet, consectetur adipiscing elit. Curabitur nec nisl odio. Mauris vehicula at nunc id posuere. Lorem ipsum dolor sit amet, consectetur adipiscing elit. Curabitur nec nisl odio. Mauris vehicula at nunc id posuere. Lorem ipsum dolor sit amet, consectetur adipiscing elit. Curabitur nec nisl odio. Mauris vehicula at nunc id posuere. Lorem ipsum dolor sit amet, consectetur adipiscing elit. Curabitur nec nisl odio. Mauris vehicula at nunc id posuere. Lorem ipsum dolor sit amet, consectetur adipiscing elit. Curabitur nec nisl odio. Mauris vehicula at nunc id posuere. Lorem ipsum dolor sit amet, consectetur adipiscing elit. Curabitur nec nisl odio. Mauris vehicula at nunc id posuere. Lorem ipsum dolor sit amet, consectetur adipiscing elit. Curabitur nec nisl odio. Mauris vehicula at nunc id posuere.</p>
</section>

<section class="block services">
  <h2 class="heading" style="top:100px">See Our Services</h2>
  <p class="lead" style="top:184px">Lorem ipsum dolor sit amet, consectetur adipiscing elit. Curabitur nec nisl odio. Mauris vehicula at nunc id posuere.</p>

  <article class="service" style="left:113px">
    <svg width="56" height="48" viewBox="0 0 56 48" aria-hidden="true"><path d="M2 8a4 4 0 0 1 4-4h16l6 6h22a4 4 0 0 1 4 4v28a4 4 0 0 1-4 4H6a4 4 0 0 1-4-4z" fill="#2a2c30"/></svg>
    <h4 class="service-title">Data Center<br>Solutions</h4>
    <p class="service-text" style="top:178px">Lorem ipsum dolor sit amet, consectetur adipiscing elit. Curabitur nec nisl odio. Mauris vehicula at nunc id posuere.</p>
  </article>
  <article class="service" style="left:363px">
    <svg width="60" height="48" viewBox="0 0 60 48" aria-hidden="true"><path d="M14 44a12 12 0 0 1-1-24 17 17 0 0 1 32-4 13 13 0 0 1 2 28z" fill="#2a2c30"/></svg>
    <h4 class="service-title">Cloud Services</h4>
    <p class="service-text" style="top:152px">Lorem ipsum dolor sit amet, consectetur adipiscing elit. Curabitur nec nisl odio. Mauris vehicula at nunc id posuere.</p>
  </article>
  <article class="service" style="left:614px">
    <svg width="56" height="48" viewBox="0 0 56 48" aria-hidden="true"><path d="M4 26l8-8 10 10L44 6l8 8-30 30z" fill="#2a2c30"/></svg>
    <h4 class="service-title">Security &amp; Risk<br>Management</h4>
    <p class="service-text" style="top:178px">Lorem ipsum dolor sit amet, consectetur adipiscing elit. Curabitur nec nisl odio. Mauris vehicula at nunc id posuere.</p>
  </article>
  <article class="service" style="left:864px">
    <svg width="56" height="52" viewBox="0 0 56 52" aria-hidden="true"><g transform="translate(28 26)" fill="#2a2c30"><circle r="16"/><rect x="-5" y="-24" width="10" height="48" rx="2"/><rect x="-5" y="-24" width="10" height="48" rx="2" transform="rotate(45)"/><rect x="-5" y="-24" width="10" height="48" rx="2" transform="rotate(90)"/><rect x="-5" y="-24" width="10" height="48" rx="2" transform="rotate(135)"/><circle r="7" fill="#e2e6ec"/></g></svg>
    <h4 class="service-title">Clean Code</h4>
    <p class="service-text" style="top:152px">Lorem ipsum dolor sit amet, consectetur adipiscing elit. Curabitur nec nisl odio. Mauris vehicula at nunc id posuere.</p>
  </article>
</section>

<section class="block queries">
  <h2 class="heading" style="top:100px">Queries ? Ask Us Now.</h2>
  <p class="lead" style="top:184px">Lorem ipsum dolor sit amet, consectetur adipiscing elit. Curabitur nec nisl odio. Mauris vehicula at nunc id posuere.</p>
</section>

<section class="block contact">
  <h4 class="contact-title">Our Contact Details</h4>
  <ul class="contact-list">
    <li><svg width="16" height="14" viewBox="0 0 16 14"><path d="M8 0l8 7h-2v7h-4V9H6v5H2V7H0z" fill="#3a3d42"/></svg>Address: some addres</li>
    <li><svg width="14" height="14" viewBox="0 0 14 14"><path d="M3 0l3 4-2 2a8 8 0 0 0 4 4l2-2 4 3-2 3C6 14 0 8 0 2z" fill="#3a3d42"/></svg>Phone: 12-345-567-899</li>
    <li><svg width="17" height="13" viewBox="0 0 17 13"><rect x="1" y="1" width="15" height="11" fill="none" stroke="#3a3d42" stroke-width="1.6"/><path d="M1 1l7.5 6L16 1" fill="none" stroke="#3a3d42" stroke-width="1.6"/></svg>E-Mail: email@yourdomain.com</li>
  </ul>
  <div class="social"><span></span><span></span><span></span><span></span><span></span></div>

  <h4 class="form-title">Lorem ipsum dolor sit amet</h4>
  <p class="form-copy">Lorem ipsum dolor sit amet, consectetur adipiscing elit. Curabitur nec nisl odio. Mauris vehicula at nunc id posuere. Lorem ipsum dolor sit amet, consectetur adipiscing elit. Curabitur nec nisl odio. Mauris vehicula at nunc id posuere.</p>
  <div class="field" style="left:527px;top:189px;width:273px;height:27px">Name</div>
  <div class="field" style="left:827px;top:189px;width:273px;height:27px">Email address</div>
  <div class="field" style="left:527px;top:231px;width:573px;height:60px">Message</div>
  <div class="button">Submit Request</div>
</section>

<footer class="block footer">
  <p class="footer-note">2017 www.yourdomain.com &nbsp;|&nbsp; All Right Reserved</p>
</footer>

</body>
</html>
```